Termite Rack Card 4 x 9 or 3.5 x 8.5

You will see an older version of the HarborTermiteRack Card this will need to be modernized with the look and branding feel of the 2024HarborFlyer file that is attached.

Remove the following verbiage from the older version- FREE TERMITE INSPECTIONS- BEST PRICES SHOULD BE REPLACED WITH COMPETITIVE PRICES- Remove paragraph our 50 Certified Master inspectors and Our Harbor Group Termite Division provides Free... Remove we will beat any fumigation or legtimate repair.

The following verbiage on one side.

Protect your Client's greatest asset with a Pre-Listing Termite Inspection

Speed up the Sales Process - By having the seller conduct a termite inspection, you reduce the risk of delays or complications. With this essential step complete, you can expedite the transaction timeline and close deals faster!

Enhance Property Value - Uncovering and remedying termite problems early can prevent costly damages and preserve the integrity of the home. With a clean bill of health from a termite inspection, you can market the property with confidence!

Boost Buyer Confidence - A pre-listing termite inspection demonstrates proactive care for the property, instilling trust in potential buyers. Identifying issues upfront, you also eliminate surprises during negotiations, leading to smoother transactions and happier clients.

The Following Bullet points on the opposite side-
HARBOR GROUP
TERMITE SOLUTIONS

*Pre-Listing Inspections
*Inspection
*Treatment
*Repairs
*Fumigations
*Bill Repairs through Escrow
*Over 40 Years Experience
*Modern and effective treatmetns
*Quality and Integrity

```html
<!DOCTYPE html>
<html lang="en">
<head>
<meta charset="utf-8">
<title>Harbor Group Termite Rack Card</title>
<link rel="stylesheet" href="https://fonts.googleapis.com/css2?family=Roboto:wght@700;900&family=Roboto+Condensed:wght@700&family=Montserrat:wght@800;900&family=Quicksand:wght@500;600;700&family=Cinzel:wght@500;600&display=swap">
<style>
:root{
  --blue:#0a84cf;
  --blue-veil:rgba(14,140,220,0.82);
  --yellow:#fff23a;
  --yellow-ink:#f7ec2a;
  --white:#ffffff;
  --pale:#cfe3f5;
  --grey-band:#cfd4da;
  --ink-blue:#0d7fd0;
}
*{margin:0;padding:0;box-sizing:border-box}
html,body{width:1200px;height:2700px;overflow:hidden;background:var(--blue)}
.card{position:relative;width:1200px;height:2700px;overflow:hidden;background:var(--blue)}
.layer{position:absolute;left:0;top:0}
.headline,.tagline,.sub{position:absolute;left:0;width:1200px;text-align:center;white-space:nowrap;line-height:1}
.headline{top:112px;font-family:"Roboto",sans-serif;font-size:182px;font-weight:900;color:var(--yellow);letter-spacing:-3px;text-shadow:6px 6px 0 var(--pale)}
.tagline{top:304px;font-family:"Roboto",sans-serif;font-size:118px;font-weight:700;color:var(--white);letter-spacing:1px}
.sub{top:422px;font-family:"Roboto Condensed",sans-serif;font-size:66px;font-weight:700;color:var(--white)}
.sub .hl{color:var(--yellow)}
.pitch{position:absolute;left:207px;width:784px;font-family:"Quicksand",sans-serif;color:var(--white)}
.pitch-title{top:652px;font-size:41px;font-weight:700;color:var(--yellow);line-height:42px;text-align:left}
.pitch-title .line1{display:block;text-align:justify;text-align-last:justify}
.pitch-body{font-size:32px;font-weight:500;line-height:33.4px;text-align:justify;text-align-last:left}
.p1{top:768px}.p2{top:968px}.p3{top:1202px}
.services{position:absolute;left:0;width:1200px;text-align:center;font-family:"Montserrat",sans-serif;white-space:nowrap}
.services-title{top:1586px;font-size:47px;font-weight:900;color:var(--yellow);line-height:46px;text-shadow:2px 3px 4px rgba(0,0,0,.45)}
.services-lead{top:1708px;font-size:40px;font-weight:800;color:var(--white);text-shadow:2px 3px 4px rgba(0,0,0,.5)}
.service-list{position:absolute;left:0;top:1778px;width:1200px;list-style:none;text-align:center;font-family:"Quicksand",sans-serif;font-weight:700;font-size:37px;text-shadow:2px 2px 4px rgba(0,0,0,.55)}
.service-list li{height:58.5px;line-height:50px;position:relative;white-space:nowrap}
.service-list li::before{content:"";position:absolute;left:596px;top:-8px;width:8px;height:8px;border-radius:50%;background:var(--white)}
.service-list li:nth-child(odd){color:var(--yellow-ink)}
.service-list li:nth-child(even){color:var(--white)}
.closing{position:absolute;left:0;width:1200px;text-align:center;font-family:"Cinzel",serif;color:var(--ink-blue);line-height:1;white-space:nowrap}
.closing-a{top:2340px;font-size:92px;font-weight:600}
.closing-b{top:2446px;font-size:64px;font-weight:600}
.phone{top:2522px;font-size:80px;font-weight:500}
.license{position:absolute;left:0;top:2615px;width:1200px;text-align:center;font-family:"Quicksand",sans-serif;font-size:41px;font-weight:500;color:var(--ink-blue)}
</style>
</head>
<body>
<main class="card">
  <svg class="layer" width="1200" height="2700" viewBox="0 0 1200 2700">
    <defs>
      <linearGradient id="houseTone" x1="0" y1="0" x2="0" y2="1">
        <stop offset="0" stop-color="#5aa9d6"/>
        <stop offset="0.45" stop-color="#8a9ba6"/>
        <stop offset="0.7" stop-color="#6f6a58"/>
        <stop offset="1" stop-color="#3f5a36"/>
      </linearGradient>
    </defs>
    <rect class="house-photo" role="img" aria-label="Photo of a modern two-storey home with glass balconies, palms and landscaped garden" x="0" y="400" width="1200" height="1880" fill="url(#houseTone)"/>
    <polygon class="pitch-veil" points="0,400 1200,400 1200,1410 600,1545 0,1410" fill="var(--blue-veil)"/>
    <polygon class="header-rim" points="0,0 1200,0 1200,420 600,628 0,420" fill="var(--pale)"/>
    <polygon class="header-band" points="0,0 1200,0 1200,405 600,610 0,405" fill="var(--blue)"/>
    <polyline class="pitch-frame" points="158,495 158,1422 600,1530 1041,1422 1041,495" fill="none" stroke="var(--white)" stroke-width="2.5"/>
    <polyline class="list-bracket" points="262,1643 207,1643 207,2130" fill="none" stroke="var(--white)" stroke-width="2.5"/>
    <polyline class="list-bracket" points="936,1643 991,1643 991,2130" fill="none" stroke="var(--white)" stroke-width="2.5"/>
    <polygon class="footer-rim" points="0,2105 600,2310 1200,2105 1200,2700 0,2700" fill="var(--grey-band)"/>
    <polygon class="footer-band" points="0,2122 600,2328 1200,2122 1200,2700 0,2700" fill="var(--yellow)"/>
    <polyline class="list-chevron" points="460,2242 600,2292 740,2242" fill="none" stroke="var(--white)" stroke-width="2.5"/>
    <line class="phone-rule" x1="0" y1="2567" x2="280" y2="2567" stroke="var(--ink-blue)" stroke-width="3"/>
    <line class="phone-rule" x1="920" y1="2567" x2="1200" y2="2567" stroke="var(--ink-blue)" stroke-width="3"/>
  </svg>

  <h1 class="headline">WHEN YOU</h1>
  <p class="tagline">THINK TERMITE,</p>
  <p class="sub">THINK <span class="hl">THE HARBOR GROUP</span></p>

  <h2 class="pitch pitch-title"><span class="line1">Protect your Client's greatest asset</span>with a Pre-Listing Termite Inspection</h2>
  <p class="pitch pitch-body p1">Speed up the Sales Process - By having the seller conduct a termite inspection, you reduce the risk of delays or complications. With this essential step complete, you can expedite the transaction timeline and close deals faster!</p>
  <p class="pitch pitch-body p2">Enhance Property Value - Uncovering and remedying termite problems early can prevent costly damages and preserve the integrity of the home. With a clean bill of health from a termite inspection, you can market the property with confidence!</p>
  <p class="pitch pitch-body p3">Boost Buyer Confidence - A pre-listing termite inspection demonstrates proactive care for the property, instilling trust in potential buyers. Identifying issues upfront, you also eliminate surprises during negotiations, leading to smoother transactions and happier clients.</p>

  <h2 class="services services-title">HARBOR GROUP<br>TERMITE SOLUTIONS</h2>
  <p class="services services-lead">PRE-LISTING INSPECTIONS</p>
  <ul class="service-list">
    <li>INSPECTION</li>
    <li>TREATMENT</li>
    <li>REPAIRS</li>
    <li>FUMIGATIONS</li>
    <li>BILL REPAIRS THROUGH ESCROW</li>
    <li>OVER 40 YEARS EXPERIENCE</li>
    <li>MODERN AND EFFECTIVE TREATMETNS</li>
    <li>QUALITY AND INTEGRITY</li>
  </ul>

  <p class="closing closing-a">THINK QUALTIY,</p>
  <p class="closing closing-b">THINK THE HARBOR GROUP</p>
  <p class="closing phone">1-800-555-0148</p>
  <p class="license">Licensed and Insured Lic #PR4120</p>
</main>
</body>
</html>
```